Halvorsen Basin Holdings, LP Letter Head

We need an official company letter head design that is clean and mimics our company logo style. It will include our logo, address, phone, and website. We are an OIl and Gas mineral purchasing company, so hints of oil rigs or related design would be desirable.

Industry/Entity Type

Oil And Gas

Colors
ec1f27
f04a50
f59195
fbd4d5

Requirements
Must have
• Logo
• 7316 Marwick T. Ellsbury Parkway, Suite 418
• Dallas TX, 75391
• 214-763-1957
• www.halvorsenbasin.com
Nice to have
• Oil Rigs or OIl and gas related design

```html
<!DOCTYPE html>
<html lang="en">
<head>
<meta charset="utf-8">
<title>Halvorsen Basin Holdings, LP Letterhead</title>
<link href="https://fonts.googleapis.com/css2?family=Cinzel:wght@400;500&family=Roboto:wght@700&display=swap" rel="stylesheet">
<style>
  :root {
    --red: #ec1f27;
    --red-soft: #f04a50;
    --pink: #f59195;
    --blush: #fbd4d5;
    --paper: #ffffff;
    --backdrop: #e4eaeb;
  }
  * { margin: 0; padding: 0; box-sizing: border-box; }
  html, body {
    width: 1131px; height: 1200px; overflow: hidden;
    background: var(--backdrop);
  }
  .letterhead {
    position: absolute; left: 132px; top: 40px;
    width: 866px; height: 1120px;
    background: var(--paper);
    box-shadow: 0 4px 14px rgba(0,0,0,0.18);
    overflow: hidden;
  }
  .brand-mark {
    position: absolute; left: 40px; top: 40px;
    display: flex; align-items: center; gap: 8px;
  }
  .brand-mark__square {
    width: 40px; height: 40px; background: var(--red);
  }
  .brand-mark__name {
    font-family: "Cinzel", serif; font-weight: 500;
    font-size: 15px; color: var(--red); line-height: 1.1;
  }
  .header-rule {
    position: absolute; left: 330px; top: 96px;
    width: 470px; height: 3px; background: var(--red);
  }
  .company {
    position: absolute; left: 330px; top: 108px; width: 470px;
    text-align: center; color: var(--red);
  }
  .company__name {
    font-family: "Cinzel", serif; font-weight: 500;
    font-size: 30px; letter-spacing: 1px; line-height: 1;
  }
  .company__tagline {
    font-family: "Cinzel", serif; font-weight: 400;
    font-size: 12px; letter-spacing: 6px; margin-top: 4px;
  }
  .contact {
    font-family: "Roboto", Arial, sans-serif; font-weight: 700;
    font-size: 12.5px; line-height: 1.35; margin-top: 8px;
  }
  .watermark {
    position: absolute; left: 383px; top: 510px;
    width: 100px; height: 100px;
    border: 3px solid var(--blush); background: rgba(251,212,213,0.25);
  }
  .edge-band {
    position: absolute; top: 0; right: 0; height: 100%;
    width: 22px; display: flex;
  }
  .edge-band__line { width: 6px; background: var(--red); }
  .edge-band__fill { flex: 1; background: var(--pink); }
  .corner-bracket {
    position: absolute; left: 0; bottom: 0;
  }
</style>
</head>
<body>
  <main class="letterhead">
    <div class="brand-mark">
      <span class="brand-mark__square"></span>
      <span class="brand-mark__name">Halvorsen<br>Basin</span>
    </div>

    <div class="header-rule"></div>
    <header class="company">
      <h1 class="company__name">Halvorsen</h1>
      <p class="company__tagline">BASIN HOLDINGS</p>
      <address class="contact">
        214-763-1957<br>
        www.halvorsenbasin.com<br>
        7316 Marwick T. Ellsbury Parkway, Suite 418 Dallas TX, 75391
      </address>
    </header>

    <div class="watermark" aria-hidden="true"></div>

    <div class="edge-band" aria-hidden="true">
      <span class="edge-band__line"></span>
      <span class="edge-band__fill"></span>
    </div>

    <svg class="corner-bracket" width="120" height="90" viewBox="0 0 120 90" aria-hidden="true">
      <path d="M0 0 H20 V70 H120 V90 H0 Z" fill="var(--red)"/>
    </svg>
  </main>
</body>
</html>
```